KTR Civils*

we are a construction company specialising in Housing, Water Infrastructure and Roadworks
This is the description I would like to be added to the Flyer. I have
also attached a Picture
Ktr Civils is a Construction Company specializing in Housing, Roadworks
and Water infrastructure. Ktr has established itself firmly in the
Construction industry with branches all through Southern Africa as well
as into Africa.
Ktr is committed to giving its Clients efficient and Professional
service at all times, We pride ourselves on our ability to meet
deadlines and exceed expectations. Our aim is to establish Successful
Long lasting relationships with our Client base
Colors
Designer to choose only greyscale colors for use in the design.
Look and feel

```html
<!DOCTYPE html>
<html lang="en">
<head>
<meta charset="utf-8">
<title>KTR Civils Flyer</title>
<link rel="stylesheet" href="https://fonts.googleapis.com/css2?family=Roboto:wght@300;400;700;900&display=swap">
<style>
  :root {
    --page-bg: #f7f7f9;
    --paper-light: #ececec;
    --panel: #e3e3e3;
    --band-dark: #3a3a3a;
    --ink: #111111;
    --black: #000000;
    --white: #ffffff;
    --footer-text: #cfcfcf;
    --divider: #b5b5b5;
  }
  * { margin: 0; padding: 0; box-sizing: border-box; }
  html, body {
    width: 1200px; height: 1200px; overflow: hidden;
    background: var(--page-bg);
    font-family: "Roboto", Arial, sans-serif;
  }
  .flyer {
    position: absolute; left: 213px; top: 54px;
    width: 773px; height: 1092px;
    background: var(--paper-light);
    overflow: hidden;
  }
  .hero-photo {
    position: absolute; left: 0; top: 27px; width: 773px; height: 543px;
    background: linear-gradient(180deg,
      #aebdcc 0%, #8e9fae 16%, #7d8a93 22%,
      #c9a08e 30%, #b88c7a 45%, #a78f76 58%,
      #b7a27d 66%, #9c9360 76%, #8e8a55 100%);
  }
  .top-shade {
    position: absolute; left: 0; top: 0; width: 690px; height: 91px;
    background: var(--paper-light);
  }
  .shapes { position: absolute; left: 0; top: 0; }
  .brand {
    position: absolute; left: 84px; top: 40px;
    width: 606px; height: 73px;
    background: var(--white);
    display: flex; align-items: center; justify-content: center;
    font-weight: 900; font-size: 58px; letter-spacing: 3px;
    color: var(--ink); text-transform: uppercase;
  }
  .info-panel {
    position: absolute; left: 0; top: 582px; width: 773px; height: 399px;
    background: var(--panel);
  }
  .column {
    position: absolute; top: 41px;
    font-size: 20.5px; line-height: 30.6px; color: var(--ink);
    white-space: nowrap;
  }
  .column-left { left: 68px; }
  .column-right { left: 414px; }
  .column strong { font-weight: 700; }
  .divider {
    position: absolute; left: 378px; top: 62px; width: 2px; height: 262px;
    background: linear-gradient(180deg, transparent, var(--divider) 15%, var(--divider) 85%, transparent);
  }
  .phone {
    position: absolute; left: 130px; top: 1010px;
    display: flex; align-items: center; gap: 8px;
    color: var(--footer-text); font-weight: 700; font-size: 47px; letter-spacing: 0.5px;
  }
  .web-contacts {
    position: absolute; left: 537px; top: 1018px;
    color: var(--footer-text); font-weight: 300; font-size: 18.5px; line-height: 22px;
  }
  .web-contacts span { display: flex; align-items: center; gap: 5px; }
</style>
</head>
<body>
  <div class="flyer">
    <div class="hero-photo" role="img" aria-label="Photo of a large new housing development with rows of small houses, power poles and grassland below distant hills"></div>
    <div class="top-shade"></div>

    <svg class="shapes" width="773" height="1092" viewBox="0 0 773 1092">
      <polygon points="573,4 773,4 773,22 553,22" fill="var(--band-dark)"/>
      <polygon points="150,552 712,552 680,582 0,582 0,570 140,570" fill="var(--band-dark)"/>
      <polygon points="0,972 195,972 186,981 115,981 21,1092 0,1092" fill="var(--band-dark)"/>
      <polygon points="115,981 773,981 773,1092 21,1092" fill="var(--black)"/>
    </svg>

    <div class="brand">KTR Civils</div>

    <div class="info-panel">
      <p class="column column-left"><strong>Ktr Civils</strong> is a Construction<br>Company specializing in<br>Housing, Roadworks and<br>Water infrastructure. Ktr<br>has established itself firmly<br>in the Construction industry<br>with branches all through<br>Southern Africa as well as<br>into Africa.</p>
      <div class="divider"></div>
      <p class="column column-right">Ktr is committed to giving its<br>Clients efficient and<br>Professional service at all<br>times, We pride ourselves on<br>our ability to meet deadlines<br>and exceed expectations. Our<br>aim is to establish Successful<br>Long lasting relationships with<br>our Client base</p>
    </div>

    <div class="phone">
      <svg width="34" height="34" viewBox="0 0 24 24" aria-hidden="true">
        <path d="M6.6 10.8c1.4 2.8 3.8 5.1 6.6 6.6l2.2-2.2c.3-.3.7-.4 1-.2 1.1.4 2.3.6 3.6.6.6 0 1 .4 1 1V20c0 .6-.4 1-1 1C10.6 21 3 13.4 3 4c0-.6.4-1 1-1h3.5c.6 0 1 .4 1 1 0 1.3.2 2.5.6 3.6.1.3 0 .7-.2 1L6.6 10.8z" fill="var(--footer-text)"/>
        <path d="M14 3.5a7 7 0 0 1 6.5 6.5M14 6.5a4 4 0 0 1 3.5 3.5" stroke="var(--footer-text)" stroke-width="1.6" fill="none" stroke-linecap="round"/>
      </svg>
      <span>002 5550 1928</span>
    </div>

    <div class="web-contacts">
      <span><svg width="12" height="12" viewBox="0 0 12 12" aria-hidden="true"><rect x="1" y="2.5" width="10" height="7" fill="none" stroke="var(--footer-text)" stroke-width="1.2"/><path d="M1 2.5l5 4 5-4" fill="none" stroke="var(--footer-text)" stroke-width="1.2"/></svg>info@ktrcivils.com</span>
      <span><svg width="12" height="12" viewBox="0 0 12 12" aria-hidden="true"><circle cx="6" cy="6" r="5" fill="none" stroke="var(--footer-text)" stroke-width="1.2"/><path d="M1 6h10M6 1c-2.5 3-2.5 7 0 10M6 1c2.5 3 2.5 7 0 10" fill="none" stroke="var(--footer-text)" stroke-width="1"/></svg>www.ktrcivils.com</span>
    </div>
  </div>
</body>
</html>
```